Dance Card to Provide Contact Info

I'm looking for a double sided business card to provide contact information to perspective dance partners.
One side of the card would have the words: "Yes I would love to Dance" written in an interesting and eye catching way. Below that would be the three categories I'm interested in
>Social >Exhibition >Competition
The other side of the card would include a picture of me with my Name, Phone Number, and Email Address (Dale Penwick, 210-547-2183, dale@twirlmerry.dance)
My target market is middle aged women interested in Country and Western dancing and West Coast Swing dancing. I am NOT particularly interested in Ballroom style.
Here are a few links to the type of dancing I want to do:
http://www.fpqlx.org/
http://www.prairiestepguildnetwork.com/
http://bexarridgepartnerspin.com/
Business
Contact Information for Business Card
Dale Penwick
210-547-2183
dale@twirlmerry.dance

```html
<!DOCTYPE html>
<html lang="en">
<head>
<meta charset="utf-8">
<title>Dale Penwick – Dance Card</title>
<link rel="stylesheet" href="https://fonts.googleapis.com/css2?family=Rye&family=Open+Sans:wght@400;600&display=swap">
<style>
  :root {
    --page: #ffffff;
    --measure: #3f79ad;
    --wood-dark: #0f0905;
    --wood-mid: #3a2414;
    --wood-warm: #5b3a20;
    --copper: #d4862c;
    --copper-deep: #8a4a12;
    --cream: #f6e6c6;
    --white: #ffffff;
    --rope: #b8672a;
  }
  * { box-sizing: border-box; margin: 0; padding: 0; }
  html, body { width: 1200px; height: 475px; overflow: hidden; background: var(--page); }
  .canvas { position: relative; width: 1200px; height: 475px; }

  .measure { position: absolute; left: 0; top: 0; }
  .measure text { font-family: 'Open Sans', sans-serif; font-size: 20px; fill: var(--measure); }

  .card {
    position: absolute; top: 58px; width: 494px; height: 302px; overflow: hidden;
  }
  .card--front { left: 90px; }
  .card--back { left: 615px; }

  .card__backdrop {
    position: absolute; inset: 0;
    background:
      radial-gradient(ellipse 55% 70% at 30% 55%, var(--wood-warm) 0%, var(--wood-mid) 45%, transparent 80%),
      linear-gradient(90deg, var(--wood-dark) 0%, var(--wood-mid) 40%, var(--wood-dark) 100%);
  }
  .card--back .card__backdrop {
    background:
      radial-gradient(ellipse 45% 60% at 70% 55%, var(--wood-warm) 0%, var(--wood-mid) 45%, transparent 85%),
      linear-gradient(90deg, var(--wood-dark) 0%, var(--wood-mid) 55%, var(--wood-dark) 100%);
  }

  .headline { position: absolute; left: 0; top: 0; }
  .headline text {
    font-family: 'Rye', serif; font-size: 25px; fill: var(--copper);
    stroke: var(--cream); stroke-width: 0.8px; paint-order: stroke;
  }

  .categories {
    position: absolute; right: 46px; top: 124px; list-style: none; text-align: right;
  }
  .categories li {
    font-family: 'Rye', serif; font-size: 25px; line-height: 45px; color: var(--white);
    text-shadow: 1px 2px 0 var(--copper-deep);
  }

  .name {
    position: absolute; left: 36px; top: 64px; white-space: nowrap;
    font-family: 'Rye', serif; font-weight: 400; font-size: 37px; line-height: 56px;
    color: var(--copper); text-shadow: 1px 2px 0 var(--copper-deep);
  }
  .contact {
    position: absolute; left: 32px; top: 228px;
    font-family: 'Open Sans', sans-serif; font-size: 17px; line-height: 26px; color: var(--cream);
  }

  .portrait {
    position: absolute; left: 248px; top: 27px; width: 242px; height: 266px; border-radius: 50%;
    background: radial-gradient(ellipse at 50% 45%, #a77a5c 0%, #6b4a35 45%, #2a1a10 75%);
    border: 12px solid var(--rope);
    box-shadow: 0 0 0 3px var(--copper-deep), inset 0 0 0 4px var(--copper-deep);
  }
</style>
</head>
<body>
<div class="canvas">
  <svg class="measure" width="1200" height="475" viewBox="0 0 1200 475" aria-hidden="true">
    <g stroke="var(--measure)" stroke-width="1.2" fill="none">
      <line x1="48" y1="58" x2="76" y2="58"/>
      <line x1="48" y1="360" x2="76" y2="360"/>
      <line x1="62" y1="70" x2="62" y2="145"/>
      <line x1="62" y1="270" x2="62" y2="348"/>
      <line x1="90" y1="374" x2="90" y2="412"/>
      <line x1="584" y1="374" x2="584" y2="412"/>
      <line x1="102" y1="397" x2="280" y2="397"/>
      <line x1="396" y1="397" x2="572" y2="397"/>
    </g>
    <g fill="var(--measure)">
      <polygon points="62,58 56,74 68,74"/>
      <polygon points="62,360 56,344 68,344"/>
      <polygon points="90,397 108,391 108,403"/>
      <polygon points="584,397 566,391 566,403"/>
    </g>
    <text x="71" y="208" text-anchor="middle" transform="rotate(-90 71 208)">55.00 mm</text>
    <text x="338" y="404" text-anchor="middle">90.00 mm</text>
  </svg>

  <section class="card card--front">
    <div class="card__backdrop" role="img" aria-label="Cowboy hat resting on worn leather boots with spurs before a rustic wooden wall and coiled lasso"></div>
    <svg class="headline" width="494" height="150" viewBox="0 0 494 150">
      <path id="arch" d="M 30 124 Q 248 -14 472 124" fill="none"/>
      <text><textPath href="#arch" startOffset="50%" text-anchor="middle">YES I WOULD LOVE TO DANCE</textPath></text>
    </svg>
    <ul class="categories">
      <li>SOCIAL</li>
      <li>EXHIBITION</li>
      <li>COMPETITION</li>
    </ul>
  </section>

  <section class="card card--back">
    <div class="card__backdrop" role="img" aria-label="Rustic wooden wall with boots on the floor"></div>
    <h1 class="name">DALE<br>PENWICK</h1>
    <p class="contact">210-547-2183<br>dale@twirlmerry.dance</p>
    <div class="portrait" role="img" aria-label="Portrait photo of Dale Penwick framed by a coiled lasso"></div>
  </section>
</div>
</body>
</html>
```